Dental Office Looking for Modern, simple business cards

We just acquired our logo. Now we would like to make business cards. We are a dental office with two doctors. We are husband and wife and have a small boutique dental practice in a small town. We love our patients and they are always asking us to give our business cards to their friends. Please help us make business cards :-)

Target Market(s)

30-60 yr old

Industry/Entity Type

Dental Clinic

Contact Information for Business Card

Birch Hollow Dental P.C.
Family and Cosmetic Dentistry
4827 Dunmore Rd. Schenectady NY 12309
Tel: 518 642 8817 Fax: 518 642 8830

Dr. Tomas K. Elridge DDS
Dr. Marisol Anne Whitby DDS

Font styles to use
Serif
Sans Serif

Requirements
Must have
• Simple clean design, modern, colorful. Should incorporate the logo.
Nice to have
• dental imagery ( teeth, smile, etc ...).

```html
<!DOCTYPE html>
<html lang="en">
<head>
<meta charset="utf-8">
<title>Birch Hollow Dental – Business Card</title>
<link rel="stylesheet" href="https://fonts.googleapis.com/css2?family=Crimson+Text:wght@400;600&family=Lato:wght@400&display=swap">
<style>
  :root {
    --backdrop: #4b4b4b;
    --card-white: #ffffff;
    --card-black: #050505;
    --brand-blue: #1f73bd;
    --name-grey: #7a7a7a;
    --contact-grey: #6d6d6d;
  }
  * { box-sizing: border-box; margin: 0; padding: 0; }
  html, body {
    width: 1200px; height: 1176px; overflow: hidden;
    background: var(--backdrop);
  }
  .canvas { position: relative; width: 1200px; height: 1176px; }

  .card {
    position: absolute; left: 252px; width: 676px; height: 387px;
    border-radius: 22px; overflow: hidden;
  }
  .card-front { top: 133px; background: var(--card-white); }
  .card-back {
    top: 610px;
    background: linear-gradient(160deg, #000 0%, #0a0a0a 60%, #161616 100%);
  }

  .doctor {
    position: absolute; top: 40px;
    font-family: "Crimson Text", serif;
    font-size: 21px; line-height: 28px; color: var(--name-grey);
    letter-spacing: 0.3px; text-transform: uppercase;
  }
  .doctor .degree { display: block; color: var(--brand-blue); }
  .doctor-left { left: 38px; }
  .doctor-right { right: 38px; text-align: right; }

  .brand-name {
    font-family: "Crimson Text", serif; font-weight: 600;
    color: var(--brand-blue); text-transform: uppercase; white-space: nowrap;
  }
  .card-front .brand-name {
    position: absolute; left: 38px; top: 250px;
    font-size: 30px; letter-spacing: 0.5px;
  }
  .card-back .brand-name {
    position: absolute; left: 0; right: 0; top: 160px; text-align: center;
    font-size: 48px; letter-spacing: 1px;
  }

  .contact {
    position: absolute; right: 38px; top: 198px;
    font-family: "Lato", sans-serif; font-size: 17px; color: var(--contact-grey);
    list-style: none; text-align: right;
  }
  .contact li { line-height: 28.5px; display: flex; justify-content: flex-end; align-items: center; gap: 10px; }
  .contact .icon { width: 16px; height: 16px; fill: var(--brand-blue); }
  .contact .address { line-height: 28.5px; margin-top: 4px; }

  .band {
    position: absolute; left: 0; right: 0; bottom: 0; height: 23px;
    background: var(--brand-blue);
  }
</style>
</head>
<body>
<div class="canvas">
  <section class="card card-front">
    <p class="doctor doctor-left">Dr. Tomas K. Elridge<span class="degree">DDS</span></p>
    <p class="doctor doctor-right">Dr. Marisol Anne Whitby<span class="degree">DDS</span></p>

    <p class="brand-name">Birch Hollow Dental</p>

    <ul class="contact">
      <li>518 642 8817
        <svg class="icon" viewBox="0 0 16 16" aria-hidden="true"><path d="M4 1.5l2.2 3-1.3 1.6c.8 1.8 2.2 3.3 4 4.2l1.6-1.3 3 2.1-1.2 2.6C7 13.4 2.4 8.9 1.6 3.2z"/></svg>
      </li>
      <li>518 642 8830
        <svg class="icon" viewBox="0 0 16 16" aria-hidden="true"><rect x="4" y="1.5" width="8" height="4"/><rect x="1" y="6" width="14" height="7" rx="1"/><rect x="4" y="10" width="8" height="4.5" fill="#fff"/><rect x="5" y="11" width="6" height="3"/></svg>
      </li>
      <li>youremail@here
        <svg class="icon" viewBox="0 0 16 16" aria-hidden="true"><rect x="1" y="3.5" width="14" height="9.5" rx="1"/><path d="M1.5 4.2L8 9l6.5-4.8" stroke="#fff" stroke-width="1.3" fill="none"/></svg>
      </li>
      <li class="address">4827 Dunmore Rd. Schenectady<br>NY 12309</li>
    </ul>

    <div class="band"></div>
  </section>

  <section class="card card-back">
    <p class="brand-name">Birch Hollow Dental</p>
  </section>
</div>
</body>
</html>
```